Lantern Marketing Group (LMG)

This is for my business cards. I want a Nice anfd Elegant Business Card to be Designed, Using more or less of the same colors of my logo that i have attached.i would like to have these business cards forever

Thank you

Thank you

Thank you

Contact Information for Business Card

Calvin Ortega
Lantern Marketing Group
C.(555) 482-1306
E-Mail. COrtega@lanternmgroup.example

Font styles to use
Serif
Sans Serif

Colors
d0dfed
cbcbcb
cee9f5

Requirements
Must have
• (LMG)
• Lantern Marketing Group
Nice to have
• 3D affects
Should not have
• Please try not using the flat version of the logo try and use the 3d version please

```html
<!DOCTYPE html>
<html lang="en">
<head>
<meta charset="utf-8">
<title>Lantern Marketing Group – Business Card</title>
<link rel="stylesheet" href="https://fonts.googleapis.com/css2?family=Saira:wght@500;600;700;800&display=swap">
<style>
  :root {
    --backdrop: #2b2b2b;
    --navy: #10273b;
    --navy-deep: #0c1f30;
    --brand-blue: #1b6fc6;
    --silver: #c3c6c9;
    --paper: #ffffff;
    --paper-shade: #eef0f2;
    --ink: #14283a;
  }
  html, body {
    margin: 0;
    padding: 0;
    width: 1200px;
    height: 849px;
    overflow: hidden;
    background: var(--backdrop);
    font-family: "Saira", "Arial Narrow", sans-serif;
  }
  .canvas {
    position: relative;
    width: 1200px;
    height: 849px;
  }
  .card {
    position: absolute;
    left: 285px;
    width: 630px;
    height: 360px;
    overflow: hidden;
    box-shadow: 0 12px 30px rgba(0,0,0,0.45);
  }
  /* Back side */
  .card-back {
    top: 44px;
    background: radial-gradient(ellipse at 50% 45%, #1d3c55 0%, var(--navy) 55%, var(--navy-deep) 100%);
    display: flex;
    align-items: center;
    justify-content: center;
    gap: 14px;
  }
  .card-back .brand-square {
    width: 30px;
    height: 30px;
    background: var(--silver);
  }
  .card-back .brand-name {
    color: var(--silver);
    font-weight: 700;
    font-size: 30px;
    letter-spacing: 2px;
    text-transform: uppercase;
    line-height: 1;
  }
  /* Front side */
  .card-front {
    top: 445px;
    background: linear-gradient(180deg, var(--paper) 0%, var(--paper-shade) 100%);
  }
  .front-brand {
    position: absolute;
    left: 40px;
    top: 44px;
    display: flex;
    align-items: center;
    gap: 10px;
  }
  .front-brand .brand-square {
    width: 26px;
    height: 26px;
    background: var(--brand-blue);
  }
  .front-brand .brand-name {
    color: var(--brand-blue);
    font-weight: 700;
    font-size: 17px;
    line-height: 1.1;
    letter-spacing: 1px;
    text-transform: uppercase;
  }
  .contact-band {
    position: absolute;
    left: 0;
    right: 0;
    top: 212px;
    bottom: 0;
    background: var(--navy);
  }
  .person-name {
    position: absolute;
    left: 40px;
    top: 168px;
    margin: 0;
    color: var(--ink);
    font-weight: 700;
    font-size: 23px;
    line-height: 32px;
    letter-spacing: 0.5px;
  }
  .contact-list {
    position: absolute;
    left: 40px;
    top: 238px;
    margin: 0;
    padding: 0;
    list-style: none;
    color: var(--paper);
    font-weight: 600;
    font-size: 18px;
    letter-spacing: 0.5px;
    line-height: 34px;
  }
</style>
</head>
<body>
  <main class="canvas">
    <section class="card card-back" aria-label="Business card back">
      <span class="brand-square"></span>
      <span class="brand-name">Lantern Marketing Group</span>
    </section>

    <section class="card card-front" aria-label="Business card front">
      <div class="contact-band"></div>
      <div class="front-brand">
        <span class="brand-square"></span>
        <span class="brand-name">Lantern<br>Marketing Group</span>
      </div>
      <h1 class="person-name">Calvin Ortega</h1>
      <ul class="contact-list">
        <li class="contact-phone">(555) 482-1306</li>
        <li class="contact-email">COrtega@lanternmgroup.example</li>
      </ul>
    </section>
  </main>
</body>
</html>
```